Painting Company Business Card

Brightwell Painting needs a new business card. See attachments for our logo and current card as an example.
We want to utilize the same colors in the logo, and keep all the information that is currently on it. Just need an updated and modern design.
We are open to loosing the Association Logos if it means a better design.
We are also entertaining a spot for a picture of a headshot of the person listed on the card. Head shot can be finished later.

```html
<!DOCTYPE html>
<html lang="en">
<head>
<meta charset="utf-8">
<title>Brightwell Painting – Business Card</title>
<link rel="stylesheet" href="https://fonts.googleapis.com/css2?family=Mulish:wght@400;700;800&family=Roboto:wght@500&display=swap">
<style>
  :root {
    --forest: #3d4431;
    --forest-deep: #343a2a;
    --paper: #ffffff;
    --paper-shade: #ececec;
    --ink-muted: #55594d;
    --backdrop: #e9e6e0;
    --on-forest: #ffffff;
  }
  * { box-sizing: border-box; margin: 0; padding: 0; }
  html, body {
    width: 900px; height: 1200px; overflow: hidden;
    background: var(--backdrop);
    font-family: "Mulish", sans-serif;
  }
  .canvas { position: relative; width: 900px; height: 1200px; }

  .card {
    position: absolute; left: 85px; width: 733px; height: 429px;
    border-radius: 22px; overflow: hidden;
    box-shadow: 0 6px 14px rgba(0,0,0,0.25);
  }
  .card--front {
    top: 143px;
    background: linear-gradient(160deg, var(--paper) 40%, var(--paper-shade) 100%);
  }
  .card--front .card-edge {
    position: absolute; left: 0; right: 0; bottom: 0; height: 15px;
    background: var(--forest);
  }
  .card--back { top: 633px; background: var(--forest); }

  .identity { position: absolute; left: 56px; top: 138px; }
  .identity-name {
    font-weight: 800; font-size: 25px; color: var(--forest); line-height: 1.1;
  }
  .identity-role {
    font-size: 16px; color: var(--ink-muted); margin-top: 4px;
  }

  .contact-list { position: absolute; left: 56px; top: 210px; list-style: none; }
  .contact-item {
    display: flex; align-items: center; gap: 10px;
    height: 26px; font-size: 16px; color: var(--forest-deep);
  }
  .contact-icon { width: 21px; height: 21px; flex: none; }

  .wordmark {
    position: absolute; display: flex; align-items: center; gap: 14px;
    font-weight: 800; line-height: 1.02; letter-spacing: 0.5px;
  }
  .wordmark-square { flex: none; }
  .wordmark--front { left: 400px; top: 148px; color: var(--forest); font-size: 44px; }
  .wordmark--front .wordmark-square { width: 26px; height: 26px; background: var(--forest); }
  .wordmark--back { left: 226px; top: 150px; color: var(--on-forest); font-size: 46px; }
  .wordmark--back .wordmark-square { width: 26px; height: 26px; background: var(--on-forest); }

  .services {
    position: absolute; left: 0; right: 0; top: 365px;
    display: flex; justify-content: center; gap: 18px; list-style: none;
    font-family: "Roboto", sans-serif; font-weight: 500; font-size: 19px;
    color: var(--on-forest);
  }
  .service { display: flex; align-items: center; gap: 8px; }
  .service-icon { width: 20px; height: 20px; }
</style>
</head>
<body>
<main class="canvas">

  <section class="card card--front" aria-label="Card front">
    <div class="identity">
      <p class="identity-name">Daniel Harper</p>
      <p class="identity-role">Quality Manager</p>
    </div>

    <ul class="contact-list">
      <li class="contact-item">
        <svg class="contact-icon" viewBox="0 0 20 20"><circle cx="10" cy="10" r="10" fill="#3d4431"/><path d="M6.5 5.5c.6-.5 1.3-.4 1.6.1l1 1.6c.3.5.1 1-.3 1.3l-.6.4c.5 1.2 1.5 2.2 2.7 2.7l.4-.6c.3-.4.8-.6 1.3-.3l1.6 1c.5.3.6 1 .1 1.6-1 1.1-2.5 1.2-4.2.1-1.5-1-2.6-2.1-3.6-3.6-1.1-1.7-1-3.2.1-4.2z" fill="#fff"/></svg>
        <span>262-555-0148</span>
      </li>
      <li class="contact-item">
        <svg class="contact-icon" viewBox="0 0 20 20"><circle cx="10" cy="10" r="10" fill="#3d4431"/><rect x="5" y="6.5" width="10" height="7" rx="0.8" fill="#fff"/><path d="M5.3 7l4.7 3.6L14.7 7" fill="none" stroke="#3d4431" stroke-width="1.1"/></svg>
        <span>daniel.harper@brightwellmail.com</span>
      </li>
      <li class="contact-item">
        <svg class="contact-icon" viewBox="0 0 20 20"><circle cx="10" cy="10" r="10" fill="#3d4431"/><g fill="none" stroke="#fff" stroke-width="1.1"><circle cx="10" cy="10" r="5.2"/><ellipse cx="10" cy="10" rx="2.3" ry="5.2"/><path d="M4.8 10h10.4M5.6 7.4h8.8M5.6 12.6h8.8"/></g></svg>
        <span>www.brightwellpainting.com</span>
      </li>
    </ul>

    <div class="wordmark wordmark--front">
      <span class="wordmark-square"></span>
      <span>Brightwell<br>Painting</span>
    </div>

    <div class="card-edge"></div>
  </section>

  <section class="card card--back" aria-label="Card back">
    <div class="wordmark wordmark--back">
      <span class="wordmark-square"></span>
      <span>Brightwell<br>Painting</span>
    </div>

    <ul class="services">
      <li class="service"><svg class="service-icon" viewBox="0 0 20 20"><path d="M11 2l7 7-3 3-7-7z M7 7l6 6-2 2-6-6z M6 12l2 2-5 5-2-2z" fill="#fff"/></svg>Exterior Painting</li>
      <li class="service"><svg class="service-icon" viewBox="0 0 20 20"><path d="M11 2l7 7-3 3-7-7z M7 7l6 6-2 2-6-6z M6 12l2 2-5 5-2-2z" fill="#fff"/></svg>Interior Painting</li>
      <li class="service"><svg class="service-icon" viewBox="0 0 20 20"><path d="M11 2l7 7-3 3-7-7z M7 7l6 6-2 2-6-6z M6 12l2 2-5 5-2-2z" fill="#fff"/></svg>Carpentry</li>
      <li class="service"><svg class="service-icon" viewBox="0 0 20 20"><path d="M11 2l7 7-3 3-7-7z M7 7l6 6-2 2-6-6z M6 12l2 2-5 5-2-2z" fill="#fff"/></svg>Drywall</li>
    </ul>
  </section>

</main>
</body>
</html>
```